ultra-minimalist business card

front (black background, matte):

tarik b. hosseny
writer | photographer
get@tarikhosseny.com

back (white background, matte):

a picture speaks a thousand words;
a word draws a thousand pictures.

www.tarikhosseny.com

all text should be small (white or silver - as long as it shows against the black - on the front; black or gray - as long as it shows against the white - on the back).

feel free to get creative in terms of arrangement, alignment, and font type, but remember, the overall style is minimalist, so nothing too fancy, please.

thanks.

```html
<!DOCTYPE html>
<html lang="en">
<head>
<meta charset="utf-8">
<title>Tarik B. Hosseny — Business Card</title>
<link rel="stylesheet" href="https://fonts.googleapis.com/css2?family=Open+Sans:wght@300;400&display=swap">
<style>
  :root {
    --backdrop: #e8e5e1;
    --card-dark: #3a3a3a;
    --card-light: #ffffff;
    --silver: #b9b9b9;
    --silver-dim: #a0a0a0;
    --ink: #1e1e1e;
    --card-shadow: 0 6px 18px rgba(0, 0, 0, 0.18);
  }
  * { margin: 0; padding: 0; box-sizing: border-box; }
  html, body {
    width: 1200px;
    height: 1000px;
    overflow: hidden;
    background: var(--backdrop);
    font-family: "Open Sans", Arial, sans-serif;
  }
  .canvas {
    position: relative;
    width: 1200px;
    height: 1000px;
  }
  .card {
    position: absolute;
    left: 266px;
    width: 666px;
    height: 397px;
    border-radius: 24px;
    box-shadow: var(--card-shadow);
  }
  .card--front { top: 74px; background: var(--card-dark); }
  .card--back  { top: 533px; background: var(--card-light); }

  .identity {
    position: absolute;
    left: 58px;
    top: 160px;
  }
  .identity__name {
    font-weight: 400;
    font-size: 35px;
    line-height: 1;
    color: var(--silver);
    letter-spacing: 0.2px;
  }
  .identity__role {
    margin-top: 9px;
    margin-left: 3px;
    font-weight: 400;
    font-size: 18px;
    line-height: 1;
    letter-spacing: 2px;
    color: var(--silver);
  }
  .contact {
    position: absolute;
    left: 372px;
    top: 186px;
    display: flex;
    align-items: center;
    font-size: 18px;
    line-height: 1;
    color: var(--silver-dim);
  }
  .contact__divider {
    width: 2px;
    height: 18px;
    background: var(--silver);
    margin-right: 26px;
  }
  .contact__email { letter-spacing: 1.3px; }

  .motto {
    position: absolute;
    top: 173px;
    left: 0;
    width: 100%;
    text-align: center;
    font-size: 18px;
    line-height: 32px;
    color: var(--ink);
  }
  .website {
    position: absolute;
    top: 347px;
    left: 0;
    width: 100%;
    text-align: center;
    font-size: 18px;
    line-height: 1;
    letter-spacing: 5.4px;
    color: var(--ink);
  }
</style>
</head>
<body>
  <main class="canvas">
    <section class="card card--front" aria-label="Card front">
      <div class="identity">
        <h1 class="identity__name">Tarik B. Hosseny</h1>
        <p class="identity__role">Writer / Photographer</p>
      </div>
      <p class="contact">
        <span class="contact__divider" aria-hidden="true"></span>
        <span class="contact__email">get@tarikhosseny.com</span>
      </p>
    </section>

    <section class="card card--back" aria-label="Card back">
      <p class="motto">A picture speaks a thousand words;<br>A word draws a thousand pictures.</p>
      <p class="website">www.tarikhosseny.com</p>
    </section>
  </main>
</body>
</html>
```